INCOME TAX SERVIES AMERICAN THEME

SOMETHING SIMILAR TO IMAGE IM PROVIDING NOT SURE IF ITS NEEDS TO BE CODED OR UNCODED I JUST NEED IT TO WORK WITH WEEBLY.

Industry/Entity Type

Work

Coding

Coded - Design and coding required

Number of Pages Required

5+ page

Colors
0355a3
ffffff
ec1f27

Requirements
Must have
• MUST BE COMPATIBLE WITH WEEBLY
Nice to have
• WOULD LIKE THE FOOTER TO SIMILAR TO PIXELHARBOR PAGE.

```html
<!DOCTYPE html>
<html lang="en">
<head>
<meta charset="utf-8">
<title>Liberty Ledger Tax</title>
<link href="https://fonts.googleapis.com/css2?family=Open+Sans:wght@400;600;700;800&display=swap" rel="stylesheet">
<style>
:root{
  --blue:#0355a3;
  --blue-dark:#023f7a;
  --red:#ec1f27;
  --white:#ffffff;
  --ink:#333a44;
  --muted:#7a8290;
  --light:#eef1f5;
  --footer:#2b2f36;
  --footer-deep:#1f2227;
}
*{box-sizing:border-box;margin:0;padding:0}
html,body{width:721px;height:1200px;overflow:hidden}
body{font-family:"Open Sans",Arial,sans-serif;color:var(--ink);background:var(--white);font-size:7px;line-height:1.5}
.page{position:relative;width:721px;height:1200px}

/* header */
.header{height:30px;position:relative;background:var(--white)}
.brand{position:absolute;left:96px;top:4px;font-weight:800;font-size:17px;color:var(--red);line-height:1;display:flex;align-items:center;gap:6px}
.brand .dot{width:12px;height:12px;background:var(--blue);border-radius:50%}
.contact-top{position:absolute;right:96px;top:9px;display:flex;align-items:center;gap:4px;font-size:7px;color:var(--blue);font-weight:600}
.social-sq{width:9px;height:9px;background:var(--red);border-radius:1px}
.nav{position:absolute;left:280px;right:0;top:30px;height:16px;background:var(--blue);display:flex;align-items:center;gap:30px;padding-left:26px}
.nav a{color:var(--white);text-decoration:none;font-size:6px;font-weight:600;text-transform:uppercase}
.nav-strip{position:absolute;left:0;right:0;top:44px;height:3px;background:var(--red)}

/* hero */
.hero{position:absolute;top:47px;left:0;right:0;height:190px;background:linear-gradient(100deg,#3c4a5c 0%,#6c7c90 45%,#c7d2de 100%)}
.hero-copy{position:absolute;left:96px;top:54px;width:230px;color:var(--white)}
.hero-copy h1{font-size:21px;font-weight:800;line-height:1.05;text-transform:uppercase}
.hero-copy p{margin-top:8px;font-size:6px;color:#e4e9ef}
.arrow{position:absolute;top:85px;width:14px;height:18px;color:var(--white)}
.arrow.l{left:68px}.arrow.r{right:68px}

/* feature cards */
.cards{position:absolute;top:250px;left:96px;width:529px;height:100px;display:flex;gap:4px;background:var(--white);box-shadow:0 2px 8px rgba(0,0,0,.18);padding:4px}
.card{flex:1;position:relative}
.card .photo{position:absolute;inset:0;background:linear-gradient(135deg,#8c96a3,#d8dde4)}
.card .label{position:absolute;left:0;bottom:0;width:70%;background:var(--red);color:var(--white);padding:4px 6px;font-size:6px}
.card .label b{display:block;font-size:7px}
.card.mid{background:var(--blue);color:var(--white);text-align:center;padding-top:14px}
.card.mid .icon{width:22px;height:22px;margin:0 auto}
.card.mid h3{font-size:8px;margin-top:4px}
.card.mid p{font-size:5.5px;padding:0 20px;color:#d4e2f2}
.btn-small{display:inline-block;margin-top:5px;border:1px solid var(--white);padding:1px 8px;font-size:5.5px}

/* what we do */
.what{position:absolute;top:368px;left:96px;width:529px;text-align:center}
.section-title{font-size:13px;font-weight:700;text-transform:uppercase;color:var(--ink)}
.rule{width:30px;height:2px;background:var(--red);margin:4px auto 6px}
.what .lead{font-size:6.5px;color:var(--ink)}
.what .body{margin-top:6px;font-size:6px;color:var(--muted);text-align:left;line-height:1.7}
.btn{display:inline-block;margin-top:12px;background:var(--red);color:var(--white);font-size:6px;font-weight:600;padding:4px 14px;border-radius:2px}

/* services */
.services{position:absolute;top:540px;left:0;right:0;height:160px;background:linear-gradient(180deg,var(--blue),var(--blue-dark));color:var(--white);text-align:center}
.services .section-title{color:var(--white);margin-top:22px}
.services .rule{background:var(--white)}
.service-row{display:flex;justify-content:center;gap:28px;margin-top:10px}
.service{width:110px}
.service .circ{width:36px;height:36px;border-radius:50%;margin:0 auto;display:flex;align-items:center;justify-content:center;border:3px solid var(--white)}
.circ.red{background:var(--red)}.circ.blue{background:#2b79c4}
.service h4{font-size:6.5px;margin-top:6px;text-transform:uppercase}
.service p{font-size:5.5px;color:#cfdcec;margin-top:2px}

/* news + testimonials */
.lower{position:absolute;top:718px;left:96px;width:529px;display:flex;gap:26px}
.col{flex:1}
.col-title{font-size:11px;font-weight:700;color:var(--blue);text-transform:uppercase;border-bottom:1px solid #dde2e8;padding-bottom:4px}
.news-item{display:flex;gap:6px;margin-top:10px}
.news-thumb{width:40px;height:32px;background:linear-gradient(135deg,#7d8896,#c5ccd5);position:relative;flex:none}
.news-date{position:absolute;left:0;bottom:0;background:var(--blue);color:var(--white);font-size:5px;padding:0 3px}
.news-item h5{font-size:6.5px;color:var(--ink)}
.news-item p{font-size:5.5px;color:var(--muted)}
.quote{margin-top:10px;border:1px solid #dde2e8;padding:6px 8px;font-size:5.5px;color:var(--muted);font-style:italic}
.author{display:flex;align-items:center;gap:6px;margin-top:8px}
.avatar{width:22px;height:22px;border-radius:50%;background:linear-gradient(135deg,#c8a48c,#8d6e5b)}
.author b{font-size:6px;color:var(--red);font-style:normal}
.author span{font-size:5.5px;color:var(--muted)}
.dots{display:flex;gap:3px;justify-content:flex-end;margin-top:-8px}
.dots i{width:5px;height:5px;border-radius:50%;background:#c7ccd3}
.dots i.on{background:var(--blue)}

/* partners */
.partners{position:absolute;top:865px;left:0;right:0;height:55px;background:var(--light);text-align:center}
.partners p{font-size:5.5px;color:var(--muted);padding-top:6px}
.badge-row{display:flex;justify-content:center;align-items:center;gap:20px;margin-top:8px}
.badge{width:58px;height:16px;background:#b9c0c9;border-radius:2px}
.badge.round{width:18px;height:18px;border-radius:50%}
.pager{width:10px;height:10px;border-radius:50%;background:#c7ccd3}

/* footer */
.footer{position:absolute;top:920px;left:0;right:0;height:245px;background:var(--footer);color:#b7bcc4}
.footer-inner{position:absolute;left:96px;top:28px;width:529px;display:flex;gap:24px}
.f-brand{width:170px}
.f-brand .brand{position:static;font-size:15px}
.f-brand h6{color:var(--white);font-size:8px;margin-top:22px}
.f-brand p{font-size:5.5px;margin-top:3px}
.newsletter{display:flex;margin-top:6px}
.newsletter span{flex:1;height:12px;background:#3a3f47}
.newsletter b{width:28px;height:12px;background:var(--red);color:var(--white);font-size:5.5px;text-align:center;line-height:12px}
.f-col{flex:1}
.f-col h6{color:var(--white);font-size:8px;font-weight:700}
.f-col .rule{margin:4px 0 8px;width:20px}
.f-col li{list-style:none;font-size:6px;margin-bottom:5px}
.f-contact li{display:flex;gap:4px;align-items:flex-start}
.f-contact i{width:6px;height:6px;background:var(--red);border-radius:50%;flex:none;margin-top:2px}
.bottom{position:absolute;bottom:0;left:0;right:0;height:35px;background:var(--footer-deep);color:#8b919a;font-size:5.5px}
.bottom .copy{position:absolute;left:96px;top:13px}
.bottom .copy b{color:var(--red);font-weight:600}
.follow{position:absolute;right:96px;top:11px;display:flex;align-items:center;gap:3px}
.follow i{width:9px;height:9px;background:#4a505a;border-radius:1px}
</style>
</head>
<body>
<div class="page">

  <header class="header">
    <div class="brand"><span class="dot"></span>Liberty Ledger Tax</div>
    <div class="contact-top">
      <svg width="8" height="8" viewBox="0 0 10 10"><path d="M2 1l2 2-1 1.5c.6 1.2 1.4 2 2.5 2.5L7 6l2 2-1.5 1.5C4 9 1 6 .5 2.5z" fill="#0355a3"/></svg>
      (555) 014 2290
      <span class="social-sq"></span><span class="social-sq"></span><span class="social-sq"></span><span class="social-sq"></span>
    </div>
  </header>
  <nav class="nav">
    <a>Home</a><a>About Us</a><a>Services</a><a>FAQ</a><a>Testimonial</a><a>Contact Us</a>
  </nav>
  <div class="nav-strip"></div>

  <section class="hero" role="img" aria-label="Photo of hands working on a tablet over tax documents">
    <svg class="arrow l" viewBox="0 0 14 18"><path d="M10 2L3 9l7 7" stroke="#fff" stroke-width="2.5" fill="none"/></svg>
    <svg class="arrow r" viewBox="0 0 14 18"><path d="M4 2l7 7-7 7" stroke="#fff" stroke-width="2.5" fill="none"/></svg>
    <div class="hero-copy">
      <h1>Welcome to<br>Liberty Ledger Tax</h1>
      <p>Lorem ipsum dolor sit amet, consectetur adipiscing elit. Etiam porta sem malesuada magna mollis euismod, donec sed odio dui nulla vitae elit libero.</p>
    </div>
  </section>

  <section class="cards">
    <div class="card">
      <div class="photo" role="img" aria-label="Photo of a business meeting at a desk"></div>
      <div class="label"><b>Lorem Ipsum</b>Dolor sit amet elit</div>
    </div>
    <div class="card mid">
      <svg class="icon" viewBox="0 0 22 22"><circle cx="11" cy="11" r="10" fill="none" stroke="#fff" stroke-width="1.5"/><path d="M11 5v12M8 8h5a2 2 0 010 4H9a2 2 0 000 4h5" stroke="#fff" stroke-width="1.5" fill="none"/></svg>
      <h3>LOREM IPSUM</h3>
      <p>Dolor sit amet, consectetur adipiscing elit sed do eiusmod tempor.</p>
      <span class="btn-small">READ MORE</span>
    </div>
    <div class="card">
      <div class="photo" role="img" aria-label="Photo of a person reviewing financial charts"></div>
      <div class="label"><b>Lorem Ipsum</b>Dolor sit amet elit</div>
    </div>
  </section>

  <section class="what">
    <h2 class="section-title">What We Do</h2>
    <div class="rule"></div>
    <p class="lead">Lorem ipsum dolor sit amet consectetur adipiscing elit.</p>
    <p class="body">Lorem ipsum dolor sit amet, consectetur adipiscing elit. Etiam porta sem malesuada magna mollis euismod. Donec sed odio dui, nulla vitae elit libero, a pharetra augue. Cras mattis consectetur purus sit amet fermentum. Vivamus sagittis lacus vel augue laoreet rutrum faucibus dolor auctor. Maecenas faucibus mollis interdum. Integer posuere erat a ante venenatis dapibus posuere velit aliquet. Aenean lacinia bibendum nulla sed consectetur. Curabitur blandit tempus porttitor. Nullam quis risus eget urna mollis ornare vel eu leo. Praesent commodo cursus magna, vel scelerisque nisl consectetur et. Fusce dapibus tellus ac cursus commodo, tortor mauris condimentum nibh, ut fermentum massa justo sit amet risus.</p>
    <span class="btn">Read More</span>
  </section>

  <section class="services">
    <h2 class="section-title">Our Services</h2>
    <div class="rule"></div>
    <div class="service-row">
      <div class="service">
        <div class="circ red"><svg width="16" height="16" viewBox="0 0 16 16"><rect x="3" y="7" width="10" height="8" rx="1" fill="#fff"/><path d="M5 7V5a3 3 0 016 0v2" stroke="#fff" stroke-width="1.5" fill="none"/></svg></div>
        <h4>Lorem Ipsum Dolor</h4>
        <p>Sit amet consectetur adipiscing elit sed do eiusmod tempor.</p>
      </div>
      <div class="service">
        <div class="circ blue"><svg width="16" height="16" viewBox="0 0 16 16"><rect x="1" y="3" width="14" height="9" rx="1" fill="none" stroke="#fff" stroke-width="1.5"/><path d="M5 14h6" stroke="#fff" stroke-width="1.5"/></svg></div>
        <h4>Lorem Ipsum Dolor</h4>
        <p>Sit amet consectetur adipiscing elit sed do eiusmod tempor.</p>
      </div>
      <div class="service">
        <div class="circ blue"><svg width="16" height="16" viewBox="0 0 16 16"><rect x="2" y="9" width="3" height="5" fill="#fff"/><rect x="6.5" y="6" width="3" height="8" fill="#fff"/><rect x="11" y="3" width="3" height="11" fill="#fff"/></svg></div>
        <h4>Lorem Ipsum Dolor</h4>
        <p>Sit amet consectetur adipiscing elit sed do eiusmod tempor.</p>
      </div>
      <div class="service">
        <div class="circ blue"><svg width="16" height="16" viewBox="0 0 16 16"><path d="M3 8l3 3 7-7" stroke="#fff" stroke-width="2" fill="none"/></svg></div>
        <h4>Lorem Ipsum Dolor</h4>
        <p>Sit amet consectetur adipiscing elit sed do eiusmod tempor.</p>
      </div>
    </div>
  </section>

  <section class="lower">
    <div class="col">
      <h3 class="col-title">Latest News</h3>
      <div class="news-item">
        <div class="news-thumb" role="img" aria-label="News photo of office paperwork"><span class="news-date">12 JAN</span></div>
        <div><h5>Lorem ipsum dolor sit amet consectetur</h5><p>Etiam porta sem malesuada magna mollis euismod donec sed odio dui.</p></div>
      </div>
      <div class="news-item">
        <div class="news-thumb" role="img" aria-label="News photo of a calculator and forms"><span class="news-date">08 JAN</span></div>
        <div><h5>Lorem ipsum dolor sit amet</h5><p>Etiam porta sem malesuada magna mollis euismod donec sed odio dui.</p></div>
      </div>
    </div>
    <div class="col">
      <h3 class="col-title">Testimonials</h3>
      <div class="quote">Lorem ipsum dolor sit amet, consectetur adipiscing elit. Etiam porta sem malesuada magna mollis euismod. Donec sed odio dui, nulla vitae elit libero a pharetra augue.</div>
      <div class="author">
        <div class="avatar" role="img" aria-label="Client portrait"></div>
        <div><b>Lorem Ipsum</b><br><span>Client, lorem company</span></div>
      </div>
      <div class="dots"><i class="on"></i><i></i><i></i></div>
    </div>
  </section>

  <section class="partners">
    <p>We are Participating Providers for the Insurance Plans</p>
    <div class="badge-row">
      <span class="pager"></span>
      <span class="badge round"></span>
      <span class="badge"></span>
      <span class="badge"></span>
      <span class="badge"></span>
      <span class="badge"></span>
      <span class="pager"></span>
    </div>
  </section>

  <footer class="footer">
    <div class="footer-inner">
      <div class="f-brand">
        <div class="brand"><span class="dot"></span>Liberty Ledger Tax</div>
        <h6>Newsletter</h6>
        <p>Sign up to get our latest tax tips.</p>
        <div class="newsletter"><span></span><b>GO</b></div>
      </div>
      <div class="f-col">
        <h6>Main menu</h6><div class="rule"></div>
        <ul><li>Home</li><li>About Us</li><li>Services</li><li>FAQ</li><li>Contact</li></ul>
      </div>
      <div class="f-col">
        <h6>Main menu</h6><div class="rule"></div>
        <ul><li>Home</li><li>About Us</li><li>Services</li><li>FAQ</li><li>Contact</li></ul>
      </div>
      <div class="f-col f-contact">
        <h6>Contact us</h6><div class="rule"></div>
        <ul>
          <li><i></i>418 Harbor Lane, Suite 2, Springfield</li>
          <li><i></i>(555) 014 2290</li>
          <li><i></i>hello@libertyledger.example</li>
        </ul>
      </div>
    </div>
    <div class="bottom">
      <div class="copy">© 2024 <b>Liberty Ledger Tax</b>. All rights reserved. Site by PIXELHARBOR | Privacy | Terms</div>
      <div class="follow">Follow Us <i></i><i></i><i></i><i></i><i></i></div>
    </div>
  </footer>

</div>
</body>
</html>
```